Road Construction Company needs business cards

We would like a new business card designed for our business.

We're a road construction company based in Qld, Australia.

Can the business card please have the following information on it.

Name: Brent Malvoy
Position: General Manager
Phone: 0471 592 304
Email: Brent.malvoy@quendix.com.au
Address: 87 Harrowgate Ave, Pindarra, QLD, 4000
Website: www.quendix.com.au

Visually we'd like the card to be professional and simple.

Attached is our logo.

Our website is www.quendix.com.au

Target Market(s)

Men aged 25-60

Contact Information for Business Card

As listed in project description

Font styles to use
Serif

Requirements
Must have
• Large logo on back of card

```html
<!DOCTYPE html>
<html lang="en">
<head>
<meta charset="utf-8">
<title>Quendix Road Construction – Business Card</title>
<link rel="stylesheet" href="https://fonts.googleapis.com/css2?family=Poppins:wght@600;700;800&display=swap">
<style>
  :root {
    --backdrop: #fcc8ec;
    --navy-deep: #0a1a45;
    --navy: #0b1f5c;
    --royal: #0a2a9a;
    --bright-blue: #1a6ee0;
    --band: #06204a;
    --logo-blue: #0d4aa8;
    --logo-light: #2a8ee0;
    --white: #ffffff;
  }
  * { margin: 0; padding: 0; box-sizing: border-box; }
  html, body {
    width: 926px; height: 1200px; overflow: hidden;
    background: var(--backdrop);
    font-family: "Poppins", sans-serif;
  }
  .card {
    position: absolute; overflow: hidden;
  }
  .card--back { left: 67px; top: 69px; width: 788px; height: 509px; }
  .card--front { left: 63px; top: 620px; width: 795px; height: 510px; }

  .photo-backdrop { position: absolute; inset: 0; }
  .card--back .photo-backdrop {
    background:
      radial-gradient(ellipse at 55% 5%, #5a6a98 0%, rgba(40,60,120,0.6) 30%, transparent 60%),
      linear-gradient(180deg, #1b2a5e 0%, #0f2a88 65%, #081a80 100%);
  }
  .card--front .photo-backdrop {
    background:
      radial-gradient(ellipse at 8% 35%, #1a78e8 0%, rgba(20,100,220,0.6) 25%, transparent 55%),
      linear-gradient(100deg, #0c3fa0 0%, #0b2a78 45%, #0c1f55 75%, #0a1a45 100%);
  }

  .ring { position: absolute; border-radius: 50%; border: 1.2px solid rgba(255,255,255,0.85); }
  .card--back .ring { left: 116px; top: -27px; width: 560px; height: 560px; }
  .card--back .disc {
    position: absolute; left: 182px; top: 39px; width: 428px; height: 428px;
    border-radius: 50%; background: var(--white);
  }
  .logo { position: absolute; text-align: center; }
  .logo__name {
    display: block; font-weight: 800; color: var(--logo-blue);
    letter-spacing: 1px; line-height: 1;
  }
  .logo__tag {
    display: block; font-weight: 600; color: var(--logo-light);
    text-transform: uppercase; line-height: 1;
  }
  .card--back .logo { left: 0; width: 792px; top: 228px; }
  .card--back .logo__name { font-size: 42px; }
  .card--back .logo__tag { font-size: 9px; letter-spacing: 6.2px; margin-top: 5px; }

  .card--front .ring--inner { left: 194px; top: 46px; width: 430px; height: 430px; border-color: rgba(255,255,255,0.5); }
  .card--front .ring--outer { left: 126px; top: -22px; width: 566px; height: 566px; border-color: rgba(255,255,255,0.22); }
  .shapes { position: absolute; inset: 0; }
  .card--front .logo { left: 29px; top: 62px; width: 193px; }
  .card--front .logo__name { font-size: 30px; }
  .card--front .logo__tag { font-size: 7px; letter-spacing: 3.1px; margin-top: 3px; }

  .person { position: absolute; left: 0; width: 810px; top: 204px; text-align: center; color: var(--white); }
  .person__name { font-size: 44px; font-weight: 700; line-height: 1.1; }
  .person__role { font-size: 28px; font-weight: 700; line-height: 1.2; margin-top: 2px; }

  .contacts { position: absolute; left: 12px; top: 370px; list-style: none; }
  .contacts li {
    display: flex; align-items: center; height: 40px;
    color: var(--white); font-size: 20.5px; font-weight: 700;
  }
  .contacts svg { width: 31px; height: 31px; margin-right: 13px; flex: none; }

  .web { position: absolute; left: 520px; width: 275px; top: 414px; text-align: center; }
  .web__url { font-size: 20px; font-weight: 700; color: var(--band); }
  .web__social { display: flex; justify-content: center; gap: 14px; margin-top: 12px; }
  .web__social span { width: 32px; height: 32px; border-radius: 50%; background: var(--band); }
</style>
</head>
<body>

<section class="card card--back">
  <div class="photo-backdrop" role="img" aria-label="Photo of a high-rise building under construction with a crane, in dark blue tones"></div>
  <div class="ring"></div>
  <div class="disc"></div>
  <div class="logo">
    <span class="logo__name">QUENDIX</span>
    <span class="logo__tag">Road Construction</span>
  </div>
</section>

<section class="card card--front">
  <div class="photo-backdrop" role="img" aria-label="Photo of a high-rise building under construction with a crane, in blue tones"></div>
  <div class="ring ring--outer"></div>
  <div class="ring ring--inner"></div>
  <svg class="shapes" viewBox="0 0 795 510" width="795" height="510">
    <path d="M29 0 H222 V143 Q222 150 215 151 L38 165 Q29 166 29 158 Z" fill="#ffffff"/>
    <polygon points="0,306 795,420 795,510 0,510" fill="#06204a"/>
    <path d="M520 406 Q506 408 506 422 V510 H795 V366 Z" fill="#ffffff"/>
  </svg>
  <div class="logo">
    <span class="logo__name">QUENDIX</span>
    <span class="logo__tag">Road Construction</span>
  </div>

  <div class="person">
    <h1 class="person__name">Brent Malvoy</h1>
    <p class="person__role">General Manager</p>
  </div>

  <ul class="contacts">
    <li>
      <svg viewBox="0 0 32 32"><circle cx="16" cy="16" r="15" fill="#fff"/><rect x="11" y="7" width="10" height="18" rx="2" fill="none" stroke="#06204a" stroke-width="2"/><line x1="14.5" y1="22" x2="17.5" y2="22" stroke="#06204a" stroke-width="1.6"/></svg>
      0471 592 304
    </li>
    <li>
      <svg viewBox="0 0 32 32"><circle cx="16" cy="16" r="15" fill="#fff"/><path d="M16 25 C11 19 10 16 10 13.5 A6 6 0 0 1 22 13.5 C22 16 21 19 16 25 Z" fill="none" stroke="#06204a" stroke-width="2"/><circle cx="16" cy="13.5" r="2.2" fill="none" stroke="#06204a" stroke-width="1.8"/></svg>
      87 Harrowgate Ave, Pindarra, QLD, 4000
    </li>
    <li>
      <svg viewBox="0 0 32 32"><circle cx="16" cy="16" r="15" fill="#fff"/><rect x="8" y="10" width="16" height="12" rx="1" fill="none" stroke="#06204a" stroke-width="2"/><path d="M8 10 L16 17 L24 10 M8 22 L13.5 15.5 M24 22 L18.5 15.5" fill="none" stroke="#06204a" stroke-width="1.6"/></svg>
      Brent.malvoy@quendix.com.au
    </li>
  </ul>

  <div class="web">
    <p class="web__url">www.quendix.com.au</p>
    <div class="web__social"><span></span><span></span><span></span><span></span></div>
  </div>
</section>

</body>
</html>
```